Präsentationsvorlagen / Powerpoint Master for my company
Zielgruppe
Offline hardware device to manage and save passwords safely.
Aufgabenstellung
DIN A4 quer

```html
<!DOCTYPE html>
<html lang="en">
<head>
<meta charset="utf-8">
<title>Keyvane Presentation Master</title>
<link href="https://fonts.googleapis.com/css2?family=Montserrat:wght@300;400;600;700;800&display=swap" rel="stylesheet">
<style>
  :root {
    --green: #2d7a34;
    --ink: #1c1c1c;
    --footer: #141414;
    --stage: #f3f3f3;
    --sheet-top: #dcdcde;
    --sheet: #f4f4f5;
    --white: #ffffff;
    --muted: #3a3a3a;
  }
  * { box-sizing: border-box; margin: 0; padding: 0; }
  html, body { width: 909px; height: 1200px; overflow: hidden; }
  body {
    background: var(--stage);
    font-family: "Montserrat", sans-serif;
    color: var(--ink);
    position: relative;
  }
  .slide {
    position: absolute;
    width: 640px;
    height: 452px;
    overflow: hidden;
    background: linear-gradient(200deg, var(--sheet-top) 0%, var(--sheet) 40%, var(--sheet) 100%);
    box-shadow: 0 4px 14px rgba(0,0,0,.12);
  }
  .slide--small { transform: scale(.625); transform-origin: top left; }
  .slide--title-card { top: 40px; left: 44px; background: #1b1b1b; }
  .slide--two { top: 40px; left: 465px; }
  .slide--three { top: 343px; left: 44px; }
  .slide--four { top: 343px; left: 465px; }
  .slide--master { top: 670px; left: 134px; }

  .slide__wedge { position: absolute; left: 0; bottom: 0; width: 640px; height: 200px; }
  .slide__header {
    position: absolute; top: 34px; left: 35px;
    font-size: 18px; font-weight: 700; letter-spacing: .2px;
  }
  .slide__header em { font-style: normal; color: var(--green); }
  .brand {
    position: absolute; top: 26px; right: 30px;
    display: flex; align-items: center; gap: 6px;
    font-size: 24px; font-weight: 700; color: var(--ink); letter-spacing: .5px;
  }
  .brand__mark { width: 15px; height: 15px; background: var(--green); }
  .footer {
    position: absolute; left: 0; right: 0; bottom: 0; height: 24px;
    background: var(--footer);
    color: var(--white); font-size: 10px; font-weight: 700;
    padding-left: 32px; line-height: 24px;
  }
  .page-tab {
    position: absolute; right: 0; bottom: 0; width: 86px; height: 32px;
    background: var(--green); border-top-left-radius: 14px;
    color: var(--white); font-size: 15px; font-weight: 700;
    text-align: center; line-height: 30px;
  }
  .photo { position: absolute; }
  .accent { position: absolute; width: 0; height: 0; }

  .lead { position: absolute; }
  .lead__light { display: block; font-size: 22px; font-weight: 300; }
  .lead__bold { display: block; font-size: 24px; font-weight: 700; color: var(--green); }
  .body-copy { font-size: 7.5px; line-height: 1.55; color: var(--muted); margin-top: 8px; }

  .feature { position: absolute; width: 160px; }
  .feature__icon { width: 20px; height: 20px; border: 1.5px solid var(--green); border-radius: 50%; margin-bottom: 6px; }
  .feature__title { font-size: 10px; font-weight: 700; color: var(--green); }

  .title-card__photo { position: absolute; inset: 0; background: linear-gradient(135deg, #2a2a2a, #111 60%, #262626); }
  .title-card .brand { color: var(--white); top: 150px; left: 150px; right: auto; font-size: 30px; }
  .title-card__heading { position: absolute; top: 200px; left: 150px; color: var(--white); }
  .title-card__heading span { display: block; font-size: 30px; font-weight: 300; }
  .title-card__heading strong { display: block; font-size: 32px; font-weight: 800; }
  .title-card__copy { position: absolute; top: 290px; left: 150px; width: 320px; font-size: 8px; line-height: 1.5; color: #cfcfcf; }
  .title-card .page-tab { width: 120px; height: 30px; }
</style>
</head>
<body>

<section class="slide slide--small slide--title-card title-card">
  <div class="title-card__photo" role="img" aria-label="Dark monochrome office interior with silhouetted people"></div>
  <div class="brand"><span class="brand__mark"></span>Keyvane</div>
  <h1 class="title-card__heading"><span>Your Presentation</span><strong>Title Goes Here</strong></h1>
  <p class="title-card__copy">Lorem ipsum dolor sit amet, consectetur adipiscing elit, sed do eiusmod tempor incididunt ut labore et dolore magna aliqua. Ut enim ad minim veniam, quis nostrud exercitation.</p>
  <div class="page-tab"></div>
</section>

<section class="slide slide--small slide--two">
  <svg class="slide__wedge" viewBox="0 0 640 200" aria-hidden="true"><polygon points="0,110 640,15 640,200 0,200" fill="#fff"/></svg>
  <h2 class="slide__header"><em>Header</em> Goes Here</h2>
  <div class="brand"><span class="brand__mark"></span>Keyvane</div>
  <div class="lead" style="top:110px;left:35px;width:250px;">
    <span class="lead__light">Lorem</span><span class="lead__bold">Ipsum Dolor</span>
    <p class="body-copy">Lorem ipsum dolor sit amet, consectetur adipiscing elit, sed do eiusmod tempor incididunt ut labore et dolore magna aliqua. Ut enim ad minim veniam, quis nostrud exercitation.</p>
    <p class="body-copy">Lorem ipsum dolor sit amet, consectetur adipiscing elit, sed do eiusmod tempor incididunt ut labore et dolore magna aliqua. Ut enim ad minim veniam, quis nostrud exercitation.</p>
  </div>
  <div class="photo" style="top:80px;left:320px;width:280px;height:260px;background:linear-gradient(135deg,#b9c6d3,#6f7f8f 55%,#3b4650);" role="img" aria-label="Two colleagues discussing a device in an office"></div>
  <div class="accent" style="top:62px;left:545px;border-left:55px solid transparent;border-bottom:18px solid var(--green);"></div>
  <div class="accent" style="top:322px;left:320px;border-right:50px solid transparent;border-top:18px solid var(--green);"></div>
  <div class="footer">Keyvane Presentation Title 2023</div>
  <div class="page-tab">02</div>
</section>

<section class="slide slide--small slide--three">
  <svg class="slide__wedge" viewBox="0 0 640 200" aria-hidden="true"><polygon points="0,110 640,15 640,200 0,200" fill="#fff"/></svg>
  <h2 class="slide__header"><em>Header</em> Goes Here</h2>
  <div class="brand"><span class="brand__mark"></span>Keyvane</div>
  <div class="photo" style="top:72px;left:35px;width:570px;height:175px;background:linear-gradient(90deg,#a0785a,#c9a07a 40%,#8e9aa3 75%,#c8ccd0);" role="img" aria-label="Presenter speaking to a team in a brick-walled office"></div>
  <div class="accent" style="top:58px;left:550px;border-left:55px solid transparent;border-bottom:16px solid var(--green);"></div>
  <div class="accent" style="top:247px;left:35px;border-right:50px solid transparent;border-top:16px solid var(--green);"></div>
  <div class="feature" style="top:272px;left:40px;"><div class="feature__icon"></div><div class="feature__title">Lorem ipsum</div><p class="body-copy">Lorem ipsum dolor sit amet, consectetur adipiscing elit, sed do eiusmod tempor incididunt ut labore et dolore magna aliqua. Ut enim ad minim veniam, quis nostrud exercitation ullamco laboris nisi</p></div>
  <div class="feature" style="top:272px;left:240px;"><div class="feature__icon"></div><div class="feature__title">Lorem ipsum</div><p class="body-copy">Lorem ipsum dolor sit amet, consectetur adipiscing elit, sed do eiusmod tempor incididunt ut labore et dolore magna aliqua. Ut enim ad minim veniam, quis nostrud exercitation ullamco laboris nisi</p></div>
  <div class="feature" style="top:272px;left:440px;"><div class="feature__icon"></div><div class="feature__title">Lorem ipsum</div><p class="body-copy">Lorem ipsum dolor sit amet, consectetur adipiscing elit, sed do eiusmod tempor incididunt ut labore et dolore magna aliqua. Ut enim ad minim veniam, quis nostrud exercitation ullamco laboris nisi</p></div>
  <div class="footer">Keyvane Presentation Title 2023</div>
  <div class="page-tab">03</div>
</section>

<section class="slide slide--small slide--four">
  <svg class="slide__wedge" viewBox="0 0 640 200" aria-hidden="true"><polygon points="0,110 640,15 640,200 0,200" fill="#fff"/></svg>
  <h2 class="slide__header"><em>Header</em> Goes Here</h2>
  <div class="brand"><span class="brand__mark"></span>Keyvane</div>
  <div class="photo" style="top:75px;left:35px;width:270px;height:290px;background:linear-gradient(135deg,#c9d3da,#8a8f94 50%,#2e2f31);" role="img" aria-label="Hand holding a desk phone receiver"></div>
  <div class="accent" style="top:250px;left:305px;border-left:40px solid var(--green);border-top:40px solid transparent;border-bottom:40px solid transparent;"></div>
  <div class="lead" style="top:75px;left:350px;width:250px;">
    <span class="lead__light">Lorem</span><span class="lead__bold">Ipsum Dolor</span>
    <p class="body-copy">Lorem ipsum dolor sit amet, consectetur adipiscing elit, sed do eiusmod tempor incididunt ut labore et dolore magna aliqua. Ut enim ad minim veniam, quis nostrud exercitation.</p>
    <p class="body-copy">Lorem ipsum dolor sit amet, consectetur adipiscing elit, sed do eiusmod tempor incididunt ut labore et dolore magna aliqua. Ut enim ad minim veniam, quis nostrud exercitation.</p>
  </div>
  <div class="footer">Keyvane Presentation Title 2023</div>
  <div class="page-tab">04</div>
</section>

<section class="slide slide--master">
  <svg class="slide__wedge" viewBox="0 0 640 200" aria-hidden="true"><polygon points="0,110 640,15 640,200 0,200" fill="#fff"/></svg>
  <h2 class="slide__header"><em>Header</em> Goes Here</h2>
  <div class="brand"><span class="brand__mark"></span>Keyvane</div>
  <div class="footer">Keyvane Presentation Title 2023</div>
  <div class="page-tab">03</div>
</section>

</body>
</html>
```